Meadowlark Learning Growth Partners (MLGP)

This is a professional business card. Logo and picture are a must on the front of the card. I am an educational consultant. I have been consulting for the past three years for a company. I am now opening my own company. My goal for my consulting company is to eventually consult all over America.

Target Market(s)

Educators, schools, professionals

Industry/Entity Type

Consulting

Contact Information for Business Card

Picture/logo on front, simple modern design

Font styles to use
Serif

Colors
85abd2
0355a3
3176b5
cedeed

Requirements
Must have
• picture, logo,
• Odessa Pruitt, Ed.S
• address 5073 Cormorant ridge Dr. Nashville, TN 37940
• Cell:616-555-0148
• Office: 629-555-0172
• www.Mlgpedu.example
• pruittodessa@mailbox.example

```html
<!DOCTYPE html>
<html lang="en">
<head>
<meta charset="utf-8">
<title>Meadowlark Learning Growth Partners – Business Card</title>
<link rel="stylesheet" href="https://fonts.googleapis.com/css2?family=Lexend:wght@500;600&family=Oswald:wght@500&family=Open+Sans:wght@400&display=swap">
<style>
  :root {
    --navy: #0b3a82;
    --ink: #2b2b2b;
    --text: #1f1f1f;
    --paper: #ffffff;
    --backdrop: #e9edf2;
    --photo-light: #eef2f7;
    --photo-mid: #c9b48a;
    --photo-dark: #1d2433;
  }
  * { margin: 0; padding: 0; box-sizing: border-box; }
  html, body { width: 1200px; height: 1000px; overflow: hidden; }
  body { background: var(--backdrop); position: relative; font-family: "Open Sans", sans-serif; }

  .card {
    position: absolute;
    left: 266px;
    width: 666px;
    height: 397px;
    background: var(--paper);
    box-shadow: 0 2px 8px rgba(0,0,0,0.18);
    overflow: hidden;
  }
  .card--front { top: 74px; }
  .card--back { top: 533px; }

  /* Front */
  .brand-mark {
    position: absolute;
    left: 110px;
    top: 172px;
    display: flex;
    align-items: center;
    gap: 14px;
  }
  .brand-mark__dot {
    width: 54px; height: 54px;
    border-radius: 50%;
    background: var(--navy);
  }
  .brand-mark__name {
    font-family: "Lexend", sans-serif;
    font-weight: 600;
    font-size: 40px;
    letter-spacing: 1px;
    color: var(--navy);
  }
  .brand-divider {
    position: absolute;
    left: 358px;
    top: 141px;
    width: 2px;
    height: 115px;
    background: var(--navy);
  }
  .brand-fullname {
    position: absolute;
    left: 377px;
    top: 138px;
    font-family: "Lexend", sans-serif;
    font-weight: 500;
    font-size: 22px;
    line-height: 31px;
    color: var(--navy);
  }

  /* Back */
  .accent-bar {
    position: absolute;
    left: 0;
    top: 95px;
    width: 16px;
    height: 50px;
    background: var(--navy);
  }
  .person-name {
    position: absolute;
    left: 34px;
    top: 92px;
    font-family: "Oswald", sans-serif;
    font-weight: 500;
    font-size: 27px;
    letter-spacing: 0.5px;
    color: var(--ink);
    text-transform: uppercase;
  }
  .person-title {
    position: absolute;
    left: 34px;
    top: 126px;
    font-size: 16px;
    color: var(--navy);
  }
  .address {
    position: absolute;
    left: 33px;
    top: 198px;
    font-size: 15.5px;
    line-height: 24px;
    color: var(--text);
  }
  .contact-list {
    position: absolute;
    left: 32px;
    top: 259px;
    list-style: none;
    font-size: 15.5px;
    line-height: 23.5px;
    color: var(--text);
  }
  .contact-list li { display: flex; align-items: center; gap: 6px; }
  .contact-list svg { width: 15px; height: 15px; fill: var(--ink); flex: none; }

  .portrait {
    position: absolute;
    left: 298px;
    top: 26px;
    width: 352px;
    height: 371px;
    border-radius: 150px 150px 0 0;
    background: linear-gradient(180deg, var(--photo-mid) 0%, #e8d2c0 40%, var(--photo-light) 62%, var(--photo-dark) 100%);
  }
</style>
</head>
<body>

<section class="card card--front">
  <div class="brand-mark">
    <span class="brand-mark__dot"></span>
    <span class="brand-mark__name">MLGP</span>
  </div>
  <div class="brand-divider"></div>
  <div class="brand-fullname">Meadowlark<br>Learning<br>Growth<br>Partners</div>
</section>

<section class="card card--back">
  <div class="accent-bar"></div>
  <h1 class="person-name">Odessa Pruitt, Ed.S</h1>
  <p class="person-title">Founder / CEO</p>

  <p class="address">5073 Cormorant ridge Dr.<br>Nashville, TN 37940</p>

  <ul class="contact-list">
    <li>
      <svg viewBox="0 0 16 16" aria-hidden="true"><path d="M1 5c0-2 3-3 7-3s7 1 7 3v1h-3V5H4v1H1zM3 7h10l1 6H2zm5 1.5a2 2 0 100 4 2 2 0 000-4z"/></svg>
      629-555-0172
    </li>
    <li>
      <svg viewBox="0 0 16 16" aria-hidden="true"><path d="M5 1h6a1 1 0 011 1v12a1 1 0 01-1 1H5a1 1 0 01-1-1V2a1 1 0 011-1zm0 2v9h6V3zm3 10a.7.7 0 100 1.4A.7.7 0 008 13z"/></svg>
      616-555-0148
    </li>
    <li>
      <svg viewBox="0 0 16 16" aria-hidden="true"><path d="M1 4h14v9H1zm1 1l6 4 6-4v-.2H2z"/></svg>
      pruittodessa@mailbox.example
    </li>
    <li>
      <svg viewBox="0 0 16 16" aria-hidden="true"><path d="M8 1a7 7 0 100 14A7 7 0 008 1zm0 1.5c.8 0 1.7 1.6 2 4H6c.3-2.4 1.2-4 2-4zM6 8h4c-.1 2.8-1.1 5.5-2 5.5S6.1 10.8 6 8zm-3.5 0H5c0 2 .5 3.8 1 4.9A5.5 5.5 0 012.5 8zm9 0h2a5.5 5.5 0 01-3.5 4.9c.5-1.1 1-2.9 1.5-4.9zM2.6 6.5A5.5 5.5 0 016 3.1c-.5 1-.9 2.2-1 3.4zm8.4 0c-.1-1.2-.5-2.4-1-3.4a5.5 5.5 0 013.4 3.4z"/></svg>
      www.Mlgpedu.example
    </li>
  </ul>

  <div class="portrait" role="img" aria-label="Portrait photo of Odessa Pruitt in a dark blazer and white collared blouse"></div>
</section>

</body>
</html>
```